Letterhead design for BRENLOW company

I need an A4 letterhead design for my company "Brenlow Electrical Products". I need the letterhead to match my current logo and business card designs. I would like it to be colourful and match the design of the business card in terms of the flowing line of colour where the information is.  

Target Market(s)

Adults aged 20 - 50 Upper middle class.

Industry/Entity Type

It Company

Requirements
Must have
• Must be A4 size and match my current logo and business card designs. Must be clean simple and eye catching.

• Must have the following information

• Brenlow Electrical Products LTD
• 7 Dunmere Lane
• Chiswick
• London
• England
• N9 3KD
• Company No. 05413926
• VAT No. GB 731552804

• Telephone: 02036159402
• Mobile: 07815263470
• Email: info@brenlow-products.co.uk
Nice to have
• nice to have a wave of colour like the business card.
Should not have
• Should not be a different colour scheme to the business card and logo design.

```html
<!DOCTYPE html>
<html lang="en">
<head>
<meta charset="utf-8">
<title>Brenlow Electrical Products – Stationery</title>
<link href="https://fonts.googleapis.com/css2?family=Questrial&family=Open+Sans:wght@400&display=swap" rel="stylesheet">
<style>
  :root {
    --page-bg: #ffffff;
    --paper: #ffffff;
    --paper-edge: #c9ced2;
    --brand-teal: #1793b4;
    --brand-deep: #0a8fb1;
    --brand-bright: #45c6e6;
    --wave-soft: #d9edf2;
    --wave-light: #eaf6fb;
    --ink: #3a3a3a;
  }
  html, body {
    margin: 0;
    padding: 0;
    width: 1200px;
    height: 983px;
    overflow: hidden;
    background: var(--page-bg);
  }
  .stationery {
    position: relative;
    width: 1200px;
    height: 983px;
  }
  .letterhead {
    position: absolute;
    left: 55px;
    top: 52px;
    width: 670px;
    height: 867px;
    background: var(--paper);
    border: 1px solid var(--paper-edge);
    box-sizing: border-box;
    overflow: hidden;
  }
  .letterhead__header {
    position: absolute;
    left: 0;
    top: 0;
    width: 100%;
    height: 87px;
    background: linear-gradient(100deg, var(--brand-deep) 0%, var(--brand-bright) 45%, #2fb3d6 70%, var(--brand-deep) 100%);
  }
  .brand {
    position: absolute;
    font-family: "Questrial", sans-serif;
    line-height: 1;
  }
  .brand__name {
    display: block;
    font-size: 40px;
    letter-spacing: 1px;
  }
  .brand__tagline {
    display: block;
    font-size: 16px;
    margin-top: 3px;
    letter-spacing: 0.3px;
  }
  .letterhead .brand {
    left: 38px;
    top: 15px;
    color: #ffffff;
  }
  .wave {
    position: absolute;
    left: 0;
    top: 0;
  }
  .letterhead__footer {
    position: absolute;
    left: 0;
    width: 100%;
    top: 795px;
    text-align: center;
    font-family: "Open Sans", sans-serif;
    font-size: 9.5px;
    line-height: 20px;
    color: var(--ink);
  }
  .sep { margin: 0 4px; }
  .envelope {
    position: absolute;
    left: 389px;
    top: 194px;
    width: 748px;
    height: 326px;
    background: var(--paper);
    border: 1px solid var(--paper-edge);
    box-sizing: border-box;
    overflow: hidden;
  }
  .envelope .brand {
    left: 40px;
    top: 20px;
    color: var(--brand-teal);
  }
  .envelope__address {
    position: absolute;
    left: 40px;
    top: 82px;
    font-family: "Open Sans", sans-serif;
    font-size: 9.5px;
    line-height: 13px;
    color: #222;
    margin: 0;
    font-style: normal;
  }
</style>
</head>
<body>
<main class="stationery">

  <section class="letterhead" aria-label="Letterhead">
    <svg class="wave" width="670" height="867" viewBox="0 0 670 867" aria-hidden="true">
      <path d="M0,835 C130,650 400,545 670,542 L670,602 C420,600 170,700 25,867 L0,867 Z" fill="var(--wave-soft)"/>
      <path d="M60,850 C200,700 420,615 670,585 L670,602 C430,605 200,700 90,867 L55,867 Z" fill="var(--wave-light)"/>
    </svg>
    <header class="letterhead__header">
      <div class="brand">
        <span class="brand__name">BRENLOW</span>
        <span class="brand__tagline">Electrical Products</span>
      </div>
    </header>
    <footer class="letterhead__footer">
      <div>7 Dunmere Lane<span class="sep">•</span>Chiswick, London, England N9 3KD<span class="sep">•</span>Company No. 05413926<span class="sep">•</span>VAT No. GB 731552804</div>
      <div>Phone: 02036159402<span class="sep">•</span>Mobile: 07815263470<span class="sep">•</span>E-mail: info@brenlow-products.co.uk<span class="sep">•</span>Website: www.brenlow-products.co.uk</div>
    </footer>
  </section>

  <section class="envelope" aria-label="Envelope">
    <svg class="wave" width="748" height="326" viewBox="0 0 748 326" aria-hidden="true">
      <path d="M0,230 C220,290 560,200 690,0 L748,0 L748,20 C610,230 290,330 0,300 Z" fill="var(--wave-soft)"/>
      <path d="M0,255 C250,300 580,215 720,0 L735,0 C600,220 300,310 0,275 Z" fill="var(--wave-light)"/>
    </svg>
    <div class="brand">
      <span class="brand__name">BRENLOW</span>
      <span class="brand__tagline">Electrical Products</span>
    </div>
    <address class="envelope__address">7 Dunmere Lane, Chiswick<br>London, England N9 3KD</address>
  </section>

</main>
</body>
</html>
```